CD COVER DESIGN - Cobalt Drifter

looking for an album cover --- music from the Mediterranean - 2 PHOTOS ARE INCLUDED BELOW - you are welcome to use both or just one.

Target Market(s)

WORLD MUSIC

Industry/Entity Type

Artists

Font styles to use
Decorative

Colors

Designer to choose colors to be used in the design.

Requirements
Must have
• MIRO VELDANOS (artist name)
• COBALT DRIFTER (ALBUM NAME)
• ATTACHED PHOTOS (MAY USE 1 OR BOTH)
Nice to have
• IMAGERY OF THE MEDITERRANEAN

```html
<!DOCTYPE html>
<html lang="en">
<head>
<meta charset="utf-8">
<title>Cobalt Drifter — Miro Veldanos</title>
<link rel="stylesheet" href="https://fonts.googleapis.com/css2?family=Great+Vibes&display=swap">
<style>
  :root {
    --page-bg: #ffffff;
    --sky-red: #ea2a2b;
    --sun-orange: #f05a22;
    --sun-glow: #fff6d8;
    --skyline-plum: #84194f;
    --skyline-deep: #5c1040;
    --sea-rose: #d84a78;
    --sea-magenta: #bc3a72;
    --sea-deep: #a02a66;
    --tile-warm: #c5685a;
    --tile-plum: #8c2d62;
    --tile-violet: #7a3a72;
    --figure-shirt: #e6e2e6;
    --figure-grey: #8d858a;
    --figure-dark: #3a3036;
    --hub-light: #c9c9cb;
    --hub-mid: #8e8e91;
    --hub-dark: #5a5a5d;
    --title-white: #ffffff;
  }
  * { margin: 0; padding: 0; box-sizing: border-box; }
  html, body {
    width: 1200px;
    height: 769px;
    overflow: hidden;
    background: var(--page-bg);
  }
  .stage { position: relative; width: 1200px; height: 769px; }

  /* shared artwork layers */
  .artwork { position: absolute; inset: 0; background: var(--sky-red); overflow: hidden; }
  .sun-arc { position: absolute; border-radius: 50%; background: var(--sun-orange); }
  .skyline {
    position: absolute;
    background:
      radial-gradient(circle at 35% 30%, var(--sun-glow) 0 26px, transparent 27px),
      linear-gradient(180deg, transparent 0 28%, var(--skyline-plum) 28%, var(--skyline-deep) 100%);
  }
  .sea {
    position: absolute;
    background: linear-gradient(180deg, var(--sea-rose) 0%, var(--sea-magenta) 45%, var(--sea-deep) 100%);
  }
  .tile-column {
    position: absolute;
    background: linear-gradient(180deg, var(--tile-warm) 0%, var(--tile-plum) 30%, var(--tile-violet) 60%, var(--tile-plum) 100%);
    opacity: 0.9;
  }
  .artist-portrait {
    position: absolute;
    border-radius: 90px 90px 14px 14px;
    background: linear-gradient(180deg, var(--figure-shirt) 0%, var(--figure-shirt) 58%, var(--figure-grey) 72%, var(--figure-dark) 100%);
  }
  .artist-name, .album-title {
    position: absolute;
    font-family: "Great Vibes", cursive;
    font-weight: 400;
    color: var(--title-white);
    white-space: nowrap;
    line-height: 1;
  }

  /* disc */
  .disc {
    position: absolute;
    left: 522px;
    top: 61px;
    width: 624px;
    height: 624px;
    border-radius: 50%;
    overflow: hidden;
    box-shadow: 0 4px 14px rgba(0,0,0,0.2);
  }
  .disc .sun-arc { left: 150px; top: -150px; width: 330px; height: 200px; }
  .disc .skyline { left: 0; top: 120px; width: 624px; height: 232px; background-position: -60px 0; }
  .disc .sea { left: 0; top: 352px; width: 624px; height: 272px; }
  .disc .tile-column { left: 496px; top: 0; width: 128px; height: 624px; }
  .disc .artist-portrait { left: 360px; top: 44px; width: 180px; height: 580px; }
  .disc .artist-name { left: 168px; top: 52px; font-size: 33px; }
  .disc .album-title { left: 158px; top: 452px; font-size: 46px; }
  .disc-hub {
    position: absolute;
    left: 224px;
    top: 220px;
    width: 184px;
    height: 184px;
    border-radius: 50%;
    background: linear-gradient(135deg, var(--hub-light) 0%, var(--hub-mid) 50%, var(--hub-dark) 100%);
    border: 3px solid var(--hub-dark);
  }
  .disc-hole {
    position: absolute;
    left: 46px;
    top: 46px;
    width: 86px;
    height: 86px;
    border-radius: 50%;
    background: var(--hub-mid);
    box-shadow: inset 0 3px 8px rgba(0,0,0,0.45);
  }

  /* cover */
  .album-cover {
    position: absolute;
    left: 64px;
    top: 63px;
    width: 621px;
    height: 621px;
    box-shadow: 0 6px 16px rgba(0,0,0,0.28);
  }
  .album-cover .sun-arc { left: 60px; top: -200px; width: 370px; height: 258px; }
  .album-cover .skyline { left: 0; top: 60px; width: 621px; height: 224px; }
  .album-cover .sea { left: 0; top: 284px; width: 621px; height: 337px; }
  .album-cover .tile-column { left: 463px; top: 0; width: 158px; height: 621px; }
  .album-cover .artist-portrait { left: 349px; top: 29px; width: 200px; height: 566px; }
  .album-cover .artist-name { left: 37px; top: 30px; font-size: 35px; }
  .album-cover .album-title { right: 22px; top: 514px; font-size: 62px; }
</style>
</head>
<body>
  <main class="stage">
    <section class="disc" aria-label="Disc label">
      <div class="artwork">
        <div class="sun-arc"></div>
        <div class="skyline" role="img" aria-label="Silhouetted city skyline with domes and minarets against a setting sun"></div>
        <div class="sea" role="img" aria-label="Magenta-tinted sea"></div>
        <div class="tile-column" role="img" aria-label="Column of ornamental Mediterranean tile pattern"></div>
        <div class="artist-portrait" role="img" aria-label="Photo of the musician holding a qanun"></div>
        <p class="artist-name">Miro Veldanos</p>
        <p class="album-title">Cobalt Drifter</p>
      </div>
      <div class="disc-hub"><div class="disc-hole"></div></div>
    </section>

    <section class="album-cover" aria-label="Album cover">
      <div class="artwork">
        <div class="sun-arc"></div>
        <div class="skyline" role="img" aria-label="Silhouetted city skyline with domes, minarets and a ferry against a setting sun"></div>
        <div class="sea" role="img" aria-label="Magenta-tinted sea with gulls skimming the water"></div>
        <div class="tile-column" role="img" aria-label="Column of ornamental Mediterranean tile pattern"></div>
        <div class="artist-portrait" role="img" aria-label="Photo of the musician standing, holding a qanun"></div>
        <p class="artist-name">Miro Veldanos</p>
        <h1 class="album-title">Cobalt Drifter</h1>
      </div>
    </section>
  </main>
</body>
</html>
```